Mortgage Loan Program(s) for Furloughed Federal Government Workers

Mortgage Loan Program(s)
For
Furloughed Federal Government Workers

* Preserve Your Credit Rating
* Receive Cash out to Increase Savings or Consolidate Bills
* Close in 30 Days or Less
* FHA and Conventional Loan Programs
* Very Competitive Rates Available
* DC & MD Properties Only

You deserve better. Contact us today....

Office (800) 647-2914 x23
Cell (240) 486-2079
Email mkowalczyk@brightpathlending.example

Marcus Kowalczyk
Brightpath Lending Services, Inc.
NMLS #837160 / #56408

Target Market(s)

```html
<!DOCTYPE html>
<html lang="en">
<head>
<meta charset="utf-8">
<title>Mortgage Loan Program(s) for Furloughed Federal Government Workers</title>
<link rel="stylesheet" href="https://fonts.googleapis.com/css2?family=Montserrat:wght@400;500;600;700&display=swap">
<style>
  :root {
    --navy: #24323f;
    --gold: #aa9a33;
    --gold-light: #dcd296;
    --cream: #f3f1ea;
    --white: #ffffff;
    --page: #e9e9e9;
  }
  * { margin: 0; padding: 0; box-sizing: border-box; }
  html, body { width: 1200px; height: 1200px; overflow: hidden; background: var(--page); }
  body { font-family: "Montserrat", sans-serif; position: relative; }

  .flyer {
    position: absolute; left: 191px; top: 32px;
    width: 908px; height: 1262px;
    transform: scale(0.9); transform-origin: top left;
    background: var(--white); overflow: hidden;
  }

  .hero-photo {
    position: absolute; left: 0; top: 0; width: 908px; height: 752px;
    background:
      radial-gradient(ellipse at 25% 35%, #5d6c73 0%, #3e4f58 30%, transparent 55%),
      radial-gradient(ellipse at 70% 35%, #ecd3cb 0%, #e2c2b8 28%, transparent 55%),
      linear-gradient(120deg, #dfe3e4 0%, #f2efea 50%, #d8c5ad 100%);
  }

  .hero-shapes { position: absolute; left: 0; top: 0; width: 908px; height: 752px; }

  .title {
    position: absolute; left: 30px; top: 412px;
    color: var(--white); font-weight: 700; font-size: 42px; line-height: 60px;
  }

  .audience {
    position: absolute; right: 42px; top: 642px; text-align: right;
    color: var(--navy); font-size: 30px; line-height: 38px; font-weight: 400;
  }
  .audience strong { font-weight: 700; }

  .rule-light { position: absolute; left: 0; top: 752px; width: 908px; height: 16px; background: var(--gold-light); }

  .benefits {
    position: absolute; left: 0; top: 768px; width: 908px; height: 317px;
    background: linear-gradient(90deg, var(--cream) 0%, #f0ecdc 55%, #e3d9a9 78%, #c9b773 100%);
  }
  .flag-art {
    position: absolute; right: 0; top: 0; width: 300px; height: 317px;
    background: linear-gradient(160deg, rgba(210,210,215,0.6) 0%, rgba(214,160,120,0.55) 45%, rgba(230,200,140,0.5) 70%, rgba(200,170,90,0.4) 100%);
  }
  .benefit-list { position: absolute; left: 28px; top: 24px; list-style: none; }
  .benefit-list li {
    display: flex; align-items: center; gap: 10px;
    height: 36px; font-size: 20px; color: var(--navy); font-weight: 500;
    white-space: nowrap;
  }
  .benefit-list svg { width: 20px; height: 18px; flex: none; }
  .tagline {
    position: absolute; left: 28px; top: 258px;
    font-size: 26px; font-weight: 600; color: var(--navy);
  }

  .rule-gold { position: absolute; left: 0; top: 1085px; width: 730px; height: 32px; background: var(--gold); }

  .contact-bar {
    position: absolute; left: 0; top: 1117px; width: 730px; height: 145px;
    background: var(--navy); color: var(--white);
  }
  .contact-lines { position: absolute; left: 28px; top: 32px; list-style: none; }
  .contact-lines li {
    display: flex; align-items: center; gap: 9px;
    height: 27px; font-size: 16px; white-space: nowrap;
  }
  .contact-lines svg { width: 19px; height: 19px; flex: none; }
  .divider { position: absolute; left: 402px; top: 34px; width: 2px; height: 76px; background: var(--white); }
  .agent {
    position: absolute; left: 420px; top: 32px;
    font-size: 16px; line-height: 27px; white-space: nowrap;
  }
  .agent-name { color: var(--gold); font-weight: 600; }

  .brand-box {
    position: absolute; left: 730px; top: 1085px; width: 178px; height: 177px;
    background: var(--white); display: flex; align-items: center; justify-content: center; gap: 10px;
  }
  .brand-mark { width: 16px; height: 16px; background: var(--navy); flex: none; }
  .brand-name { font-weight: 700; font-size: 19px; line-height: 24px; color: var(--navy); }
</style>
</head>
<body>
  <main class="flyer">
    <div class="hero-photo" role="img" aria-label="Photo of a couple at a table reviewing mortgage paperwork together"></div>

    <svg class="hero-shapes" viewBox="0 0 908 752" aria-hidden="true">
      <polygon points="0,375 390,375 390,550 0,550" fill="#24323f" fill-opacity="0.82"/>
      <polygon points="0,550 170,550 186,598 272,752 0,752" fill="#24323f"/>
      <polygon points="170,550 390,550 420,598 186,598" fill="#24323f" fill-opacity="0.82"/>
      <polygon points="186,598 300,598 386,752 272,752" fill="#aa9a33"/>
      <polygon points="300,598 414,598 500,752 386,752" fill="#24323f"/>
      <polygon points="414,598 908,598 908,752 500,752" fill="rgba(220,224,228,0.9)"/>
    </svg>

    <h1 class="title">Mortgage Loan<br>Program(s)</h1>
    <p class="audience">For <strong>Furloughed Federal</strong><br><strong>Government</strong> Workers</p>

    <div class="rule-light"></div>

    <section class="benefits">
      <div class="flag-art" role="img" aria-label="Waving American flag fading into the background"></div>
      <ul class="benefit-list">
        <li><svg viewBox="0 0 20 18"><path d="M1 10 L7 16 L19 2" fill="none" stroke="#aa9a33" stroke-width="4"/></svg>Preserve Your Credit Rating</li>
        <li><svg viewBox="0 0 20 18"><path d="M1 10 L7 16 L19 2" fill="none" stroke="#aa9a33" stroke-width="4"/></svg>Receive Cash out to Increase Savings or Consolidate Bills</li>
        <li><svg viewBox="0 0 20 18"><path d="M1 10 L7 16 L19 2" fill="none" stroke="#aa9a33" stroke-width="4"/></svg>Close in 30 Days or Less</li>
        <li><svg viewBox="0 0 20 18"><path d="M1 10 L7 16 L19 2" fill="none" stroke="#aa9a33" stroke-width="4"/></svg>FHA and Conventional Loan Programs</li>
        <li><svg viewBox="0 0 20 18"><path d="M1 10 L7 16 L19 2" fill="none" stroke="#aa9a33" stroke-width="4"/></svg>Very Competitive Rates Available</li>
        <li><svg viewBox="0 0 20 18"><path d="M1 10 L7 16 L19 2" fill="none" stroke="#aa9a33" stroke-width="4"/></svg>DC &amp; MD Properties Only</li>
      </ul>
      <p class="tagline">You deserve better. Contact us today....</p>
    </section>

    <div class="rule-gold"></div>

    <footer class="contact-bar">
      <ul class="contact-lines">
        <li><svg viewBox="0 0 20 20"><circle cx="10" cy="10" r="10" fill="#fff"/><path d="M6 5 L8.5 5 L9.5 8 L8 9 Q9.5 12 11 12.5 L12 11 L15 12 L15 14.5 Q9 15 5.5 9 Z" fill="#24323f"/></svg>(800) 647-2914 x23</li>
        <li><svg viewBox="0 0 20 20"><circle cx="10" cy="10" r="10" fill="#fff"/><path d="M6 5 L8.5 5 L9.5 8 L8 9 Q9.5 12 11 12.5 L12 11 L15 12 L15 14.5 Q9 15 5.5 9 Z" fill="#24323f"/></svg>(240) 486-2079</li>
        <li><svg viewBox="0 0 20 20"><circle cx="10" cy="10" r="10" fill="#fff"/><rect x="5" y="6.5" width="10" height="7" fill="none" stroke="#24323f" stroke-width="1.4"/><path d="M5 6.5 L10 10.5 L15 6.5" fill="none" stroke="#24323f" stroke-width="1.4"/></svg>mkowalczyk@brightpathlending.example</li>
      </ul>
      <div class="divider"></div>
      <div class="agent">
        <div class="agent-name">Marcus Kowalczyk</div>
        <div>Brightpath Lending Services, Inc.</div>
        <div>NMLS #837160 / #56408</div>
      </div>
    </footer>

    <div class="brand-box">
      <span class="brand-mark"></span>
      <span class="brand-name">Brightpath<br>Lending</span>
    </div>
  </main>
</body>
</html>
```